Business Card Design

We need two business cards - same design but with two different people's details.

We are a new start-up online cleaning business that allows people to book and pay for a quality home cleaner online.

We would like a professional yet overly formal style of business card.

Target Market(s)

18 - 65+ professionals

Industry/Entity Type

Business

Contact Information for Business Card

We would like two business cards but with the same design, the details are below:

Peter Valdoro
Director and Co-Founder
ph: 0421 573 916
Suite 3C, Level 4
517 Harwood Road
Belmira NSW 2089
peter@tidlo.com.au

_______________________________________________________

Evangelia Valdoro
Director and Co-Founder
ph: 0432 915047
Suite 3C, Level 4
517 Harwood Road
Belmira NSW 2089
evangelia@tidlo.com.au

Requirements
Must have
• although our style guide refers to orange and red, please stick to the blue/black/grey that is in the style guide.

also on the back of the card we would like the logo with our tag line which is on page 12 of the style guide.
Should not have
• no pictures of mops, cleaners etc

```html
<!DOCTYPE html>
<html lang="en">
<head>
<meta charset="utf-8">
<title>Tidlo Business Cards</title>
<link href="https://fonts.googleapis.com/css2?family=Source+Sans+3:wght@400;600;700&display=swap" rel="stylesheet">
<style>
  :root {
    --brand-blue: #14a7e0;
    --ink: #111111;
    --charcoal: #333333;
    --paper: #ffffff;
    --page: #ffffff;
  }
  * { box-sizing: border-box; margin: 0; padding: 0; }
  html, body { width: 1200px; height: 1000px; overflow: hidden; background: var(--page); }
  .canvas { position: relative; width: 1200px; height: 1000px; }

  .card {
    position: absolute;
    width: 337px;
    height: 548px;
    border-radius: 24px;
    overflow: hidden;
    background: var(--brand-blue);
    box-shadow: 3px 5px 8px rgba(0,0,0,0.28);
    font-family: "Source Sans 3", "Myriad Pro", sans-serif;
    color: var(--ink);
  }
  .card--peter { left: 237px; top: 162px; }
  .card--evangelia { left: 597px; top: 161px; }

  .card__logo-band {
    position: absolute; left: 0; top: 70px; width: 100%; height: 154px;
    background: var(--paper);
  }
  .brand-dot {
    position: absolute; left: 50%; top: 10px; width: 70px; height: 70px;
    margin-left: -35px; border-radius: 50%; background: var(--brand-blue);
  }
  .brand-name {
    position: absolute; left: 0; right: 0; top: 98px; text-align: center;
    font-family: "Source Sans 3", sans-serif; font-weight: 700; font-size: 42px;
    line-height: 1; color: var(--charcoal);
  }

  .person { position: absolute; left: 36px; top: 286px; }
  .person__name { font-size: 25px; font-weight: 400; line-height: 1; letter-spacing: 0.2px; white-space: nowrap; }
  .person__name strong { font-weight: 700; }
  .person__role { font-size: 14px; margin: 6px 0 0 3px; }
  .person__rule {
    position: absolute; left: 31px; top: 340px; width: 269px; height: 1px;
    background: var(--charcoal);
  }

  .contact { position: absolute; left: 34px; top: 370px; list-style: none; font-size: 12.5px; }
  .contact li { display: flex; align-items: flex-start; height: 19.5px; white-space: nowrap; }
  .contact svg { width: 12px; height: 12px; margin-right: 14px; margin-top: 2px; flex: none; fill: var(--ink); }
  .contact .phone { font-weight: 700; }
  .contact .indent { padding-left: 26px; }

  .bubble-area {
    position: absolute; right: 0; bottom: 0; width: 100%; height: 120px;
    background: linear-gradient(to bottom, rgba(255,255,255,0) 0%, rgba(255,255,255,0.5) 65%, rgba(255,255,255,0.9) 100%);
  }

  .lockup { position: absolute; left: 783px; top: 848px; }
  .lockup__dot {
    position: absolute; left: 0; top: 0; width: 78px; height: 78px;
    border-radius: 50%; background: var(--brand-blue);
  }
  .lockup__name {
    position: absolute; left: 92px; top: 14px;
    font-family: "Source Sans 3", sans-serif; font-weight: 700; font-size: 42px; line-height: 1;
    color: var(--charcoal); white-space: nowrap;
  }
  .lockup__tagline {
    position: absolute; left: 93px; top: 60px; white-space: nowrap;
    font-family: "Source Sans 3", sans-serif; font-weight: 400; font-size: 13px; color: var(--charcoal);
  }
</style>
</head>
<body>
<div class="canvas">

  <article class="card card--peter">
    <div class="card__logo-band">
      <span class="brand-dot"></span>
      <div class="brand-name">Tidlo</div>
    </div>
    <div class="person">
      <h1 class="person__name"><strong>PETER</strong> VALDORO</h1>
      <p class="person__role">Director and Co-Founder</p>
    </div>
    <div class="person__rule"></div>
    <ul class="contact">
      <li class="phone"><svg viewBox="0 0 12 12"><path d="M1 4c0-2 2-3 5-3s5 1 5 3H8.5V3h-5v1zM2.5 5h7l1.5 5.5H1z"/></svg>0421 573 916</li>
      <li><svg viewBox="0 0 12 12"><path d="M0 2h12v8H0zM1 3l5 3.5L11 3z" fill-rule="evenodd"/></svg>peter@tidlo.com.au</li>
      <li><svg viewBox="0 0 12 12"><path d="M6 0a4 4 0 0 1 4 4c0 3-4 8-4 8S2 7 2 4a4 4 0 0 1 4-4zm0 2.5a1.5 1.5 0 1 0 0 3 1.5 1.5 0 0 0 0-3z"/></svg>Suite 3C, Level 4 517 Harwood Road</li>
      <li class="indent">Belmira NSW 2089</li>
    </ul>
    <div class="bubble-area" role="img" aria-label="White soap bubble decoration along the bottom of the card"></div>
  </article>

  <article class="card card--evangelia">
    <div class="card__logo-band">
      <span class="brand-dot"></span>
      <div class="brand-name">Tidlo</div>
    </div>
    <div class="person">
      <h1 class="person__name"><strong>EVANGELIA</strong> VALDORO</h1>
      <p class="person__role">Director and Co-Founder</p>
    </div>
    <div class="person__rule"></div>
    <ul class="contact">
      <li class="phone"><svg viewBox="0 0 12 12"><path d="M1 4c0-2 2-3 5-3s5 1 5 3H8.5V3h-5v1zM2.5 5h7l1.5 5.5H1z"/></svg>0432 915047</li>
      <li><svg viewBox="0 0 12 12"><path d="M0 2h12v8H0zM1 3l5 3.5L11 3z" fill-rule="evenodd"/></svg>evangelia@tidlo.com.au</li>
      <li><svg viewBox="0 0 12 12"><path d="M6 0a4 4 0 0 1 4 4c0 3-4 8-4 8S2 7 2 4a4 4 0 0 1 4-4zm0 2.5a1.5 1.5 0 1 0 0 3 1.5 1.5 0 0 0 0-3z"/></svg>Suite 3C, Level 4 517 Harwood Road</li>
      <li class="indent">Belmira NSW 2089</li>
    </ul>
    <div class="bubble-area" role="img" aria-label="White soap bubble decoration along the bottom of the card"></div>
  </article>

  <div class="lockup">
    <span class="lockup__dot"></span>
    <div class="lockup__name">Tidlo</div>
    <div class="lockup__tagline">Free your day. Book a trusted clean fast.</div>
  </div>

</div>
</body>
</html>
```